Business Card Design for Contracting

I need a Busines card design for a new Busines (sole trader) based in Sydney, Australia. The business has been set up so I can contract my services to companies. The service I provide is mainly in the civil engineering discipline with the services that can be provided being contract project management, contract estimating, contract time controls and contract financial controls. I would like the design to have the colour blue used.

Target Market(s)

Large to medium Construction companies.

Industry/Entity Type

Construction

Contact Information for Business Card

Pelloway Civil Engineering Services
P.O. Box 418
Brambleford, NSW, 2093

Mobile: 0412 958 231

Email: marcus.pelloway@pcvx.com.au
Web: PCVX.com.au

Font styles to use
Sans Serif

Colors
0493ce
34a6d7
85cae6

Requirements
Must have
• my project must have my name and qualification:
• Marcus Pelloway
• BE (Civil), MTRQAust.

```html
<!DOCTYPE html>
<html lang="en">
<head>
<meta charset="utf-8">
<title>Pelloway Civil Engineering Services – Business Card</title>
<link rel="stylesheet" href="https://fonts.googleapis.com/css2?family=Asap:wght@400;500&display=swap">
<style>
  :root {
    --stage: #0d7fbb;
    --card: #ffffff;
    --brand-red: #952a27;
    --brand-teal: #1f95b2;
    --ink: #1c1c1c;
    --on-colour: #ffffff;
  }
  html, body {
    margin: 0;
    padding: 0;
    width: 1200px;
    height: 1000px;
    overflow: hidden;
    background: var(--stage);
  }
  .business-card {
    position: absolute;
    left: 150px;
    top: 228px;
    width: 900px;
    height: 544px;
    display: block;
    font-family: "Asap", sans-serif;
  }
  .card-face { fill: var(--card); }
  .band-red { fill: var(--brand-red); }
  .band-teal { fill: var(--brand-teal); }
  .rule-red { stroke: var(--brand-red); stroke-width: 2.5; }
  .rule-teal { stroke: var(--brand-teal); stroke-width: 2.5; }
  .brand-name { fill: var(--on-colour); font-size: 13px; font-weight: 500; }
  .holder, .postal { fill: var(--ink); font-size: 13.5px; font-weight: 400; }
  .contact { fill: var(--on-colour); font-size: 13.5px; font-weight: 400; }
</style>
</head>
<body>
<svg class="business-card" viewBox="0 0 510 308" xmlns="http://www.w3.org/2000/svg" aria-label="Business card for Pelloway Civil Engineering Services">
  <rect class="card-face" x="0" y="0" width="510" height="308"/>

  <!-- header band -->
  <path class="band-red" d="M0 0 H414 Q416 0 414 8 L410 20 Q407 26 398 30 L232 106 Q226 109 216 109 H0 Z"/>
  <rect class="band-red" x="22" y="22" width="12" height="12" rx="1"/>
  <text class="brand-name" x="42" y="32">Pelloway</text>
  <text class="brand-name" x="42" y="49">Civil Engineering Services</text>

  <!-- holder -->
  <text class="holder" x="480" y="104" text-anchor="end">Marcus Pelloway</text>
  <text class="holder" x="480" y="124" text-anchor="end">BE(Civil), MTRQAust</text>
  <rect class="band-red" x="487" y="93" width="23" height="32"/>

  <!-- divider rules -->
  <line class="rule-red" x1="0" y1="149" x2="510" y2="149"/>
  <line class="rule-teal" x1="0" y1="158" x2="510" y2="158"/>

  <!-- postal address -->
  <rect class="band-teal" x="4" y="185" width="18" height="30"/>
  <text class="postal" x="30" y="196">P.O. Box 418 Brambleford,</text>
  <text class="postal" x="30" y="215">NSW, 2093</text>

  <!-- contact band -->
  <path class="band-teal" d="M96 308 V286 Q96 278 104 274 L276 201 Q283 198 292 198 H510 V308 Z"/>
  <text class="contact" x="480" y="268" text-anchor="end">Mobile: 0412 958 231</text>
  <text class="contact" x="480" y="289" text-anchor="end">Email: marcus@pelloway.net.au</text>
</svg>
</body>
</html>
```